Young Accounting firm needing a captivating business card

We need a business card design that forces the person to look at the card because its either gold foil, plastic, or lettering pop up etc. We already have a logo with a specific gold color and we need to make it pop. We are an accounting firm. I need the words" accounting, payroll, licenses, audits, taxes" somewhere on the business card so as to describe what we do- preferably on the side where the logo is at.

Industry/Entity Type

Accounting

Contact Information for Business Card

Address 48276 9th Ave S Ste 305, Federal Way, WA 98117
Business Phone (360)418-2096
Fax (360)418-2157
Office Cell Phone (360)586-7319

Font styles to use
Serif

Colors
85abd2

Requirements
Must have
• It should state
• "Accounting" "Taxes" "Audits" "Licenses" "Payroll"
Nice to have
• Matte with gold foil, different textures, With Either a textured ivory background or gray blue slate background
Should not have
• colorful colors

```html
<!DOCTYPE html>
<html lang="en">
<head>
<meta charset="utf-8">
<title>KestrelLedger Business Card</title>
<link rel="stylesheet" href="https://fonts.googleapis.com/css2?family=Fira+Sans+Condensed:wght@700&family=Roboto:wght@400;500&display=swap">
<style>
  :root {
    --backdrop: #a8a8a8;
    --gold: #b8953a;
    --gold-light: #d9bd6a;
    --gold-dark: #8f6f22;
    --paper: #f1f1ef;
    --ink: #2e2e2e;
    --slate-blue: #85abd2;
  }
  * { margin: 0; padding: 0; box-sizing: border-box; }
  html, body {
    width: 1200px; height: 852px; overflow: hidden;
    background: var(--backdrop);
    font-family: "Roboto", sans-serif;
  }
  .stage { position: relative; width: 1200px; height: 852px; }
  .card {
    position: absolute; width: 500px; height: 286px;
    border-radius: 14px; overflow: hidden;
    box-shadow: 0 6px 18px rgba(0,0,0,0.25);
  }
  .card-back { left: 70px; top: 283px; }
  .pattern-fill {
    width: 100%; height: 100%;
    background: linear-gradient(135deg, var(--gold-dark) 0%, var(--gold-light) 45%, var(--gold) 70%, var(--gold-dark) 100%);
  }
  .card-front { left: 630px; top: 283px; background: var(--paper); color: var(--ink); }
  .brand {
    position: absolute; right: 28px; top: 60px;
    display: flex; align-items: center; gap: 8px;
  }
  .brand-square { width: 22px; height: 22px; background: var(--gold); }
  .brand-name { font-size: 30px; font-weight: 500; color: var(--gold); letter-spacing: -0.5px; line-height: 36px; }
  .holder { position: absolute; left: 30px; top: 108px; }
  .holder-name {
    font-family: "Fira Sans Condensed", sans-serif; font-weight: 700;
    font-size: 20px; line-height: 24px; color: var(--gold);
  }
  .holder-title { font-size: 12px; line-height: 16px; margin-top: 2px; }
  .address {
    position: absolute; right: 28px; top: 112px;
    font-size: 11.5px; line-height: 16px; text-align: right;
  }
  .services {
    position: absolute; right: 28px; top: 152px;
    font-size: 10px; line-height: 14px; letter-spacing: 0.6px;
    text-transform: uppercase; color: var(--gold); font-weight: 500;
    text-align: right;
  }
  .contacts { position: absolute; left: 30px; top: 172px; list-style: none; }
  .contacts li {
    display: flex; align-items: center; gap: 10px;
    font-size: 12px; line-height: 17px;
  }
  .contacts svg { width: 11px; height: 11px; fill: var(--gold); flex: none; }
  .edge-band { position: absolute; left: 0; bottom: 0; width: 100%; height: 9px; display: flex; }
  .edge-band .band-gold { flex: 7; background: var(--gold); }
  .edge-band .band-blue { flex: 3; background: var(--slate-blue); }
  .side-band { position: absolute; right: 0; top: 96px; width: 5px; bottom: 0; background: var(--slate-blue); }
</style>
</head>
<body>
<main class="stage">
  <section class="card card-back">
    <div class="pattern-fill" role="img" aria-label="Gold foil surface with repeating brand pattern"></div>
  </section>

  <section class="card card-front">
    <div class="brand">
      <span class="brand-square"></span>
      <span class="brand-name">KestrelLedger</span>
    </div>

    <div class="holder">
      <div class="holder-name">Marisol Deverin</div>
      <div class="holder-title">Founder / President</div>
    </div>

    <div class="address">
      48276 9th Ave S Ste 305,<br>Federal Way, WA 98117
    </div>

    <p class="services">Accounting · Payroll · Licenses · Audits · Taxes</p>

    <ul class="contacts">
      <li><svg viewBox="0 0 12 12"><path d="M2 1h2l1 3-1.5 1a6 6 0 0 0 3.5 3.5L8 7l3 1v2a1 1 0 0 1-1 1A9 9 0 0 1 1 2a1 1 0 0 1 1-1z"/></svg>(360)418-2096</li>
      <li><svg viewBox="0 0 12 12"><path d="M3 1h6v3H3zM1 5h10v4H9v2H3V9H1zM4 8v2h4V8z"/></svg>(360)418-2157</li>
      <li><svg viewBox="0 0 12 12"><path d="M3 0h6v12H3zM4 1v8h4V1z"/></svg>(360)586-7319</li>
      <li><svg viewBox="0 0 12 12"><path d="M0 2h12v8H0zM1 3l5 4 5-4z"/></svg>M.Deverin@KestrelLedger.com</li>
      <li><svg viewBox="0 0 12 12"><circle cx="6" cy="6" r="5.5"/></svg>www.KestrelLedger.com</li>
    </ul>

    <div class="side-band"></div>
    <div class="edge-band"><span class="band-gold"></span><span class="band-blue"></span></div>
  </section>
</main>
</body>
</html>
```